Logo and Label Design for New Olive Oil Brand

We need a logo and a label designed for our new Olive Oil Brand called "La Bruneva". La Bruneva means "The Evening"

Attached are some logos and labels we really like. As you can see from the logo examples, we prefer a clean, simple classic look. I thin the writing should be in red for the name "La Bruneva"

Every label will have specs about the olive listed. Those specs include:

Country: Italian
Region: Apuglia
Mono or Blend: Mono
Variety: Peranzana
Polyphenol Level: 489
Acidity: .02

These should be shown on the side of the bottle. I envision the middle of the logo being the logo, EXTRA VIRGIN OLIVE OIL, the size etc..etc.., the left side being the nutitional facts and ingredients and the right side being the specs listed above

I also attach an image of the bottle being used. it is a 500ML Velmora bottle.

Colors
ec1f27
ffffff
757575
000000

Requirements
Should not have
• gimmick type clip art

```html
<!DOCTYPE html>
<html lang="en">
<head>
<meta charset="UTF-8">
<title>La Bruneva – Garlic Extra Virgin Olive Oil Label</title>
<link rel="stylesheet" href="https://fonts.googleapis.com/css2?family=Jost:wght@400;500&display=swap">
<style>
  :root {
    --page-bg: #ffffff;
    --band-dark: #2a2a2a;
    --flavour-dark: #3a3a3a;
    --flavour-light: #5a5a5a;
    --olive-deep: #5e4115;
    --olive-warm: #8c6524;
    --olive-light: #a47a32;
    --diamond: #2b2b2b;
    --brand-red: #a81e26;
    --text-light: #ffffff;
  }
  * { margin: 0; padding: 0; box-sizing: border-box; }
  html, body {
    width: 1200px;
    height: 1000px;
    overflow: hidden;
    background: var(--page-bg);
  }
  .canvas {
    position: relative;
    width: 1200px;
    height: 1000px;
    background: var(--page-bg);
  }
  .label {
    position: absolute;
    left: 367px;
    top: 0;
    width: 465px;
    height: 1000px;
    font-family: "Jost", "Futura", sans-serif;
    color: var(--text-light);
    overflow: hidden;
  }
  .flavour-band {
    position: absolute;
    left: 0; top: 0;
    width: 100%;
    height: 160px;
    display: flex;
    align-items: center;
    justify-content: center;
  }
  .flavour-photo {
    position: absolute;
    inset: 0;
    background: radial-gradient(ellipse at 30% 40%, var(--flavour-light), var(--flavour-dark) 70%);
  }
  .flavour-name {
    position: relative;
    font-size: 38px;
    font-weight: 500;
    letter-spacing: 4px;
    margin-top: -10px;
  }
  .hero {
    position: absolute;
    left: 0; top: 160px;
    width: 100%;
    height: 600px;
  }
  .hero-photo {
    position: absolute;
    inset: 0;
    background: linear-gradient(160deg, var(--olive-light) 0%, var(--olive-warm) 40%, var(--olive-deep) 100%);
  }
  .brand-diamond {
    position: absolute;
    left: 0; top: 0;
  }
  .brand-name {
    position: absolute;
    left: 0; top: 278px;
    width: 100%;
    text-align: center;
    font-size: 52px;
    font-weight: 500;
    color: var(--brand-red);
    line-height: 1;
  }
  .product-band {
    position: absolute;
    left: 0; top: 760px;
    width: 100%;
    height: 240px;
    background: var(--band-dark);
    text-align: center;
  }
  .product-grade {
    position: absolute;
    left: 0; top: 26px;
    width: 100%;
    font-size: 44px;
    font-weight: 400;
    letter-spacing: 3px;
  }
  .product-type {
    position: absolute;
    left: 0; top: 84px;
    width: 100%;
    font-size: 66px;
    font-weight: 400;
    letter-spacing: 4px;
  }
  .product-volume {
    position: absolute;
    left: 0; top: 190px;
    width: 100%;
    font-size: 26px;
    font-weight: 500;
    letter-spacing: 3px;
  }
</style>
</head>
<body>
<main class="canvas">
  <section class="label">
    <header class="flavour-band">
      <div class="flavour-photo" role="img" aria-label="Photograph of whole garlic bulbs in grey tones"></div>
      <h2 class="flavour-name">GARLIC</h2>
    </header>

    <div class="hero">
      <div class="hero-photo" role="img" aria-label="Photograph of an olive branch with leaves in warm amber tones"></div>
      <svg class="brand-diamond" width="465" height="600" viewBox="0 0 465 600" aria-hidden="true">
        <polygon points="235,124 415,312 235,500 55,312" fill="var(--diamond)" stroke="var(--diamond)" stroke-width="24" stroke-linejoin="round"/>
      </svg>
      <h1 class="brand-name">La Bruneva</h1>
    </div>

    <footer class="product-band">
      <p class="product-grade">EXTRA VIRGIN</p>
      <p class="product-type">OLIVE OIL</p>
      <p class="product-volume">500 ML</p>
    </footer>
  </section>
</main>
</body>
</html>
```